Bright Anchor Tools and Building Supply Inc. (Rebranding)

Target Market(s)

mainly people who do DIY, and also construction companies.

Industry/Entity Type

Construction

Contact Information for Business Card

418 R. Velasco St. Brgy. 164 Sta. Lucia Manila, Philippines 1003
(02) 861-4097
www.bat.example
brightanchortools@mailbox.example

Number of Pages Required

5+ page

Font styles to use
Sans Serif

Colors
f37122
f78f20

Requirements
Must have
• to RETAIN the current logo used.
Nice to have
• ideas on how to apply the current logos to different promotional items
Should not have
• DO NOT change the Current Logo

```html
<!DOCTYPE html>
<html lang="en">
<head>
<meta charset="utf-8">
<title>Bright Anchor Tools and Building Supply Inc. — Stationery</title>
<link rel="stylesheet" href="https://fonts.googleapis.com/css2?family=Poppins:wght@400;600;700&family=PT+Serif&display=swap">
<style>
  :root {
    --stage: #3b3b3d;
    --label: #b9b9bb;
    --orange: #f26122;
    --orange-soft: #f68a55;
    --orange-pale: #fde7dc;
    --paper: #ffffff;
    --ink: #3a3a3a;
  }
  * { margin: 0; padding: 0; box-sizing: border-box; }
  html, body { width: 1200px; height: 859px; overflow: hidden; }
  body {
    position: relative;
    background: var(--stage);
    font-family: "Poppins", sans-serif;
  }
  .piece-label {
    position: absolute;
    color: var(--label);
    font-size: 16px;
    font-weight: 400;
    transform: translateX(-50%);
  }

  .brand {
    position: absolute;
    text-align: right;
    font-weight: 700;
    line-height: 1;
  }
  .brand .brand-name { display: block; }
  .brand .brand-line { display: block; font-weight: 400; margin-top: 3px; white-space: nowrap; }

  .contact {
    position: absolute;
    text-align: right;
    color: var(--paper);
    font-weight: 600;
    line-height: 1.45;
    white-space: nowrap;
  }
  .contact li { list-style: none; display: flex; justify-content: flex-end; align-items: center; gap: 4px; }
  .contact .dot {
    display: inline-block;
    flex: none;
    border-radius: 50%;
    background: var(--paper);
  }
  .contact .email { letter-spacing: 0.12em; }

  .artwork { position: absolute; }

  /* Letterhead */
  .letterhead {
    position: absolute;
    left: 59px; top: 100px;
    width: 531px; height: 684px;
    background: var(--paper);
    overflow: hidden;
    box-shadow: 0 6px 18px rgba(0,0,0,0.45);
  }
  .letterhead .header-band {
    position: absolute; left: 0; top: 77px; width: 100%; height: 41px;
    background: var(--orange);
  }
  .letterhead .brand { right: 37px; top: 22px; color: var(--orange); }
  .letterhead .brand .brand-name { font-size: 21px; }
  .letterhead .brand .brand-line { font-size: 6px; }
  .letterhead .contact { right: 37px; top: 83px; font-size: 7px; }
  .letterhead .contact .dot { width: 6px; height: 6px; }
  .letterhead .letter {
    position: absolute; left: 74px; top: 192px; width: 388px;
    font-family: "PT Serif", serif;
    font-size: 9.9px; line-height: 15.4px; color: var(--ink);
    text-align: justify;
  }
  .letterhead .letter .date { margin-bottom: 15.4px; }
  .letterhead .letter p + p { margin-top: 15.4px; }
  .letterhead .footer-band {
    position: absolute; left: 0; top: 657px; width: 100%; height: 11px;
    background: var(--orange);
  }
  .letterhead .footer-rule {
    position: absolute; left: 0; top: 672px; width: 100%; height: 2px;
    background: var(--orange);
  }

  /* Business cards */
  .card {
    position: absolute;
    top: 228px; width: 221px; height: 128px;
    background: var(--orange);
    overflow: hidden;
    box-shadow: 0 4px 12px rgba(0,0,0,0.45);
  }
  .card-front { left: 643px; }
  .card-back { left: 922px; }
  .card .brand { color: var(--paper); }
  .card-front .brand { right: 18px; top: 12px; }
  .card-front .brand .brand-name { font-size: 12px; }
  .card-front .brand .brand-line { font-size: 4px; }
  .card-front .title-band {
    position: absolute; left: 0; top: 45px; width: 100%; height: 27px;
    background: var(--orange-soft);
  }
  .card-front .holder {
    position: absolute; right: 18px; top: 47px; text-align: right; color: var(--paper);
  }
  .card-front .holder .name { display: block; font-size: 13px; font-weight: 600; line-height: 1.1; }
  .card-front .holder .role { display: block; font-size: 5px; font-weight: 600; }
  .card-front .contact { right: 18px; top: 79px; font-size: 5.6px; line-height: 1.5; }
  .card-front .contact .email { letter-spacing: 0.06em; }
  .card-front .contact .dot { width: 5px; height: 5px; }
  .card-back .brand { right: 56px; top: 45px; }
  .card-back .brand .brand-name { font-size: 16px; }
  .card-back .brand .brand-line { font-size: 4.5px; }
  .card-back .web {
    position: absolute; left: 0; width: 100%; top: 108px; text-align: center;
    color: var(--paper); font-size: 8px; font-weight: 600; letter-spacing: 0.32em;
  }

  /* Envelope */
  .envelope {
    position: absolute;
    left: 644px; top: 461px; width: 509px; height: 221px;
    background: var(--orange);
    overflow: hidden;
    box-shadow: 0 6px 16px rgba(0,0,0,0.45);
  }
  .envelope .lower-band {
    position: absolute; left: 0; top: 161px; width: 100%; height: 60px;
    background: var(--orange-soft);
  }
  .envelope .brand { right: 37px; top: 22px; color: var(--paper); }
  .envelope .brand .brand-name { font-size: 25px; }
  .envelope .brand .brand-line { font-size: 6px; }
  .envelope .contact { right: 37px; top: 169px; font-size: 8.6px; line-height: 1.5; }
  .envelope .contact .dot { width: 7px; height: 7px; }
</style>
</head>
<body>

  <span class="piece-label" style="left:309px; top:61px;">Letterhead</span>
  <span class="piece-label" style="left:900px; top:179px;">b-card</span>
  <span class="piece-label" style="left:900px; top:423px;">Envelope</span>

  <article class="letterhead">
    <svg class="artwork" style="left:0; top:18px;" width="105" height="170" role="img" aria-label="Star and stripes brand illustration">
      <rect width="105" height="170" fill="var(--orange)"/>
    </svg>
    <svg class="artwork" style="left:320px; top:360px;" width="211" height="290" role="img" aria-label="Faint star and stripes brand illustration">
      <rect width="211" height="290" fill="var(--orange-pale)" opacity="0.35"/>
    </svg>

    <div class="header-band"></div>

    <div class="brand">
      <span class="brand-name">Bright Anchor</span>
      <span class="brand-line">TOOLS AND BUILDING SUPPLY INC.</span>
    </div>

    <ul class="contact">
      <li>418 r. velasco st., brgy. 164, sta. lucia, manila 1003 <span class="dot"></span></li>
      <li>(02) 861-4097 <span class="dot"></span></li>
      <li><span class="email">brightanchortools@mailbox.example</span> <span class="dot"></span></li>
    </ul>

    <div class="letter">
      <p class="date">Sep 11 14</p>
      <p>Lorem ipsum dolor sit amet, consectetur adipiscing elit, sed do eiusmod tempor incididunt ut labore et dolore magna aliqua. Ut enim ad minim veniam, quis nostrud exercitation ullamco laboris nisi ut aliquip ex ea commodo consequat. Duis aute irure dolor in reprehenderit in voluptate velit esse cillum dolore eu fugiat nulla pariatur. Excepteur sint occaecat cupidatat non proident, sunt in culpa qui officia deserunt mollit anim id est laborum. Sed ut perspiciatis unde omnis iste natus error sit voluptatem accusantium.</p>
      <p>Nemo enim ipsam voluptatem quia voluptas sit aspernatur aut odit aut fugit, sed quia consequuntur magni dolores eos qui ratione voluptatem sequi nesciunt. Neque porro quisquam est, qui dolorem ipsum quia dolor sit amet, consectetur, adipisci velit, sed quia non numquam eius modi tempora incidunt ut labore et dolore magnam aliquam quaerat voluptatem. Ut enim ad minima veniam, quis nostrum exercitationem ullam corporis suscipit laboriosam, nisi ut aliquid ex ea commodi consequatur. Quis autem vel eum iure reprehenderit qui in ea voluptate velit esse quam nihil molestiae consequatur, vel illum qui dolorem eum fugiat quo voluptas nulla pariatur. At vero eos et accusamus et iusto odio dignissimos ducimus qui blanditiis praesentium.</p>
      <p>Temporibus autem quibusdam et aut officiis debitis aut rerum necessitatibus saepe eveniet ut et voluptates repudiandae sint et molestiae non recusandae. Itaque earum rerum hic tenetur a sapiente delectus, ut aut reiciendis voluptatibus maiores alias consequatur aut perferendis doloribus.</p>
    </div>

    <div class="footer-band"></div>
    <div class="footer-rule"></div>
  </article>

  <section class="card card-front">
    <svg class="artwork" style="left:0; top:14px;" width="72" height="100" role="img" aria-label="Star and stripes brand illustration">
      <rect width="72" height="100" fill="var(--orange-pale)"/>
    </svg>
    <div class="title-band"></div>
    <div class="brand">
      <span class="brand-name">Bright Anchor</span>
      <span class="brand-line">TOOLS AND BUILDING SUPPLY INC.</span>
    </div>
    <div class="holder">
      <span class="name">Your Name</span>
      <span class="role">CEO/OWNER</span>
    </div>
    <ul class="contact">
      <li>418 r. velasco st. <span class="dot"></span></li>
      <li>brgy. 164, sta. lucia</li>
      <li>manila 1003</li>
      <li>(02) 861-4097 <span class="dot"></span></li>
      <li><span class="email">brightanchortools@mailbox.example</span> <span class="dot"></span></li>
    </ul>
  </section>

  <section class="card card-back">
    <svg class="artwork" style="left:160px; top:20px;" width="61" height="80" role="img" aria-label="Faint star and stripes brand illustration">
      <rect width="61" height="80" fill="var(--orange-soft)" opacity="0.6"/>
    </svg>
    <div class="brand">
      <span class="brand-name">Bright Anchor</span>
      <span class="brand-line">TOOLS AND BUILDING SUPPLY INC.</span>
    </div>
    <p class="web">www.bat.example</p>
  </section>

  <section class="envelope">
    <div class="lower-band"></div>
    <svg class="artwork" style="left:0; top:8px;" width="110" height="190" role="img" aria-label="Star and stripes brand illustration">
      <rect width="110" height="190" fill="var(--orange-pale)"/>
    </svg>
    <div class="brand">
      <span class="brand-name">Bright Anchor</span>
      <span class="brand-line">TOOLS AND BUILDING SUPPLY INC.</span>
    </div>
    <ul class="contact">
      <li>418 r. velasco st., brgy. 164, sta. lucia, manila 1003 <span class="dot"></span></li>
      <li>(02) 861-4097 <span class="dot"></span></li>
      <li><span class="email">brightanchortools@mailbox.example</span> <span class="dot"></span></li>
    </ul>
  </section>

</body>
</html>
```